Wordpress Design Project - New Website for Catering Company

Thimble Hearth Catering is looking for a new and improved website to sell its Private Catering Service to London and S.E based businesses and private clients. Our current website www.thimbleuk-example.co.uk details our offerings, but it is rather plain currently and we would like something much more image focused. Attached is also our new logo.

We would like to include lots of images of lovely food (canapés, dinners, artisan breads, yummy cheeses, fresh ingredients, cakes, brownies etc) to show we are high-end chefs that produce delicious, fresh and seasonal food. We have some stock images that we have taken and own, but we are also interested in using stock photography from elsewhere. Some other catering and food websites that we like are….

www.harrowandfinch-example.com (we like the use of images on this site and the simple layout and navigation)
www.bluekettlecatering-example.co.uk (we like the use of images to illustrate the services offered)
http://www.oatandembertable-example.com/index.php?option=com_content&view=frontpage&Itemid=1 (again an image based site that we like. We also want to incorporate a 'seasonal recipe' section that we can update regularly and easily
http://marvas-larder-example.co.uk/ (we also quite like the idea of rotating images on the home page, like this site. We also like the idea of a 'less is more' homepage, that isn't overloaded with info
http://www.thebrinetable-example.com/ (we like the simple homepage on this one)

We would like the menu to run as follows…..

1) Homepage (image lead, basic info about us, quick link to seasonal recipe)

2) Services
2.1 Canapes
2.2 Working Lunches
2.3 Dinner Parties
2.4 Fork buffets
2.5 Food for Children
2.6 Celebrations (Wedding / Christenings)
2.7 Freezer Filling / Drop off Dinners
2.8 Hampers and Food Gifts
2.9 Wine Matching & Drinks

3) Staff

4) Menus
4.1 Spring/Summer Canape Menu
4.2 Autumn/Winter Canape Menu
4.3 Spring/Summer Buffet Menu
4.4 Autumn/Winter Buffet Menu
4.5 Spring/Summer Dinner Party Menu
4.6 Autumn/Winter Dinner Party Menu
4.7 Wine List

5) Seasonal Recipe

6) Testimonials & Clients

7) About us & Contact Details

We would also like to be able to update the seasonal recipe page easily and potentially also turn this in to a mail shot which we can send to clients - we'd like this integrated in to the CMS.

We currently have a twitter account - thimble cooks and a Facebook page (Thimble Hearth Catering) which we would also like to integrate in to the website.

We would like a word press or joomla site which we are able to manage easily.

Reason: I think the sites that have come through are a good start, but we are looking for something a little more high-end I think - particularly with regards to the food images used on the site.

Target Market(s)

London based companies wanting high-end catering e.g marketing agencies, lawyers, financial industries. Also private clients wanting parties

Industry/Entity Type

Catering

Requirements
Must have
• Link to our twitter and Facebook account.

Seasonal recipe page that is easy for us to update (we aren't technical at all!)

```html
<!DOCTYPE html>
<html lang="en">
<head>
<meta charset="utf-8">
<title>Thimble Hearth Catering – Home</title>
<link rel="stylesheet" href="https://fonts.googleapis.com/css2?family=Arimo:wght@400;700&family=Ubuntu:wght@400;500&display=swap">
<style>
  :root {
    --plum-deep: #3e1030;
    --plum-dark: #521640;
    --plum-mid: #8a2c6c;
    --plum-light: #9c3a7c;
    --nav-bg: #4a1238;
    --nav-active: #6a1f52;
    --leaf: #8cc85a;
    --leaf-pale: #b7dc98;
    --leaf-frame-top: #a4d07e;
    --leaf-frame-bottom: #6d9a4a;
    --ink-light: #f4eaf0;
    --ink-muted: #d2b5c6;
    --header-white: #ffffff;
    --phone-plum: #5b1d45;
    --divider: rgba(230, 200, 220, 0.55);
  }
  * { margin: 0; padding: 0; box-sizing: border-box; }
  html, body { width: 1059px; height: 1200px; overflow: hidden; }
  body {
    position: relative;
    font-family: "Arimo", Arial, sans-serif;
    color: var(--ink-light);
    background: linear-gradient(180deg, var(--plum-deep) 0%, var(--plum-dark) 14%, var(--plum-mid) 45%, var(--plum-light) 60%, var(--plum-mid) 80%, var(--plum-dark) 100%);
  }

  /* Header */
  .site-header {
    position: absolute; left: 44px; top: 16px; width: 975px; height: 171px;
    background: var(--header-white);
    border-radius: 4px;
    box-shadow: 0 0 0 3px #e9f1df, 0 3px 8px rgba(0,0,0,0.35);
  }
  .brand {
    position: absolute; left: 36px; top: 40px;
    display: flex; align-items: center; gap: 16px;
    font-family: "Ubuntu", "Trebuchet MS", sans-serif;
    font-weight: 500; font-size: 40px; line-height: 1.05;
    color: var(--leaf);
  }
  .brand-mark { width: 22px; height: 22px; background: var(--plum-dark); flex: none; }
  .social-links { position: absolute; right: 40px; top: 46px; display: flex; gap: 6px; }
  .social-links span { width: 18px; height: 18px; border-radius: 3px; background: var(--plum-mid); display: block; }
  .phone {
    position: absolute; right: 32px; top: 92px;
    display: flex; align-items: center; gap: 14px;
    font-family: "Arimo", Arial, sans-serif; font-size: 28px; color: #2a1a24;
  }
  .phone-icon { width: 34px; height: 34px; border-radius: 6px; background: var(--phone-plum); display: flex; align-items: center; justify-content: center; }

  /* Navigation */
  .main-nav {
    position: absolute; left: 44px; top: 209px; width: 975px; height: 45px;
    background: linear-gradient(180deg, #5a1a46, var(--nav-bg));
    border-radius: 3px;
  }
  .main-nav ul { list-style: none; display: flex; height: 100%; align-items: center; }
  .main-nav li { font-size: 14.5px; color: #fff; }
  .main-nav li.current {
    position: relative; align-self: flex-end;
    margin-left: 6px; width: 84px; height: 56px;
    background: var(--nav-active); color: var(--leaf);
    display: flex; align-items: center; justify-content: center; padding-top: 10px;
  }
  .main-nav li.item { margin-left: 33px; }

  /* Slider */
  .hero-slider {
    position: absolute; left: 30px; top: 276px; width: 976px; height: 418px;
    background: linear-gradient(180deg, var(--leaf-frame-top), var(--leaf-frame-bottom));
    border-radius: 3px;
  }
  .hero-image {
    position: absolute; left: 20px; top: 19px; width: 938px; height: 379px;
    border-radius: 4px;
    background: radial-gradient(ellipse 32% 42% at 33% 50%, #c8884a 0%, #d9a86e 45%, #efe3d6 80%, #ffffff 100%), #ffffff;
  }
  .slider-arrow {
    position: absolute; top: 187px; width: 42px; height: 56px;
    background: #1b1b1b; display: flex; align-items: center; justify-content: center;
  }
  .slider-arrow.prev { left: 20px; border-radius: 0 28px 28px 0; }
  .slider-arrow.next { right: 18px; border-radius: 28px 0 0 28px; }
  .slider-arrow i { width: 20px; height: 20px; border-radius: 50%; background: #e6e6e6; display: flex; align-items: center; justify-content: center; }

  /* Headings */
  .section-title {
    font-family: "Ubuntu", "Trebuchet MS", sans-serif; font-weight: 400;
    color: var(--leaf); font-size: 25px;
  }
  .title-rule { border-bottom: 1px dotted var(--divider); }

  /* Testimonials */
  .testimonials { position: absolute; left: 67px; top: 716px; width: 258px; }
  .testimonial { font-size: 13px; line-height: 23px; color: var(--ink-light); }
  .testimonial blockquote { position: relative; padding-left: 2px; }
  .testimonial .q { font-family: Georgia, serif; font-size: 24px; line-height: 0; vertical-align: -8px; }
  .testimonial cite { display: block; font-style: normal; color: var(--leaf); font-size: 13.5px; margin-top: 22px; }
  .testimonial.first { margin-top: 40px; }
  .testimonial-divider { width: 272px; margin: 26px 0 36px; border-bottom: 1px dotted var(--divider); }
  .column-divider { position: absolute; left: 339px; top: 728px; height: 403px; border-left: 1px dotted var(--divider); }

  /* Intro */
  .intro { position: absolute; left: 398px; top: 716px; width: 590px; }
  .intro .section-title { display: inline-block; padding-bottom: 8px; width: 194px; }
  .intro p { margin-top: 20px; font-size: 12.3px; line-height: 23px; color: var(--ink-light); }

  /* Seasonal recipe */
  .recipes { position: absolute; left: 398px; top: 924px; width: 640px; }
  .recipes .section-title { display: inline-block; padding-bottom: 8px; width: 278px; }
  .recipe-strip { position: absolute; left: -30px; top: 65px; width: 660px; height: 122px; }
  .recipe-thumb {
    position: absolute; top: 0; width: 182px; height: 122px;
    border: 3px solid #d6e9c3; border-radius: 4px;
  }
  .thumb-1 { left: 41px; background: radial-gradient(circle at 45% 45%, #e0b070, #f3efe9 55%, #ffffff); }
  .thumb-2 { left: 248px; background: radial-gradient(circle at 45% 55%, #b5492d, #3a3a3a 45%, #1d1d1d); }
  .thumb-3 { left: 456px; background: linear-gradient(135deg, #e8a17c, #d9735a 50%, #c45a8a); }
  .strip-arrow { position: absolute; top: 46px; }
  .strip-arrow.prev { left: 0; }
  .strip-arrow.next { right: -12px; }

  /* Footer */
  .site-footer {
    position: absolute; left: 44px; top: 1156px; width: 975px; height: 44px;
    background: var(--nav-bg); border-radius: 3px 3px 0 0;
    display: flex; justify-content: center; align-items: center; gap: 18px;
    font-size: 12.5px; color: var(--ink-muted);
  }
</style>
</head>
<body>

<header class="site-header">
  <div class="brand"><span class="brand-mark"></span><span>Thimble Hearth<br>Catering</span></div>
  <div class="social-links" aria-label="Social links"><span></span><span></span><span></span><span></span></div>
  <div class="phone">
    <span class="phone-icon">
      <svg width="20" height="20" viewBox="0 0 24 24"><path fill="#fff" d="M6.6 10.8c1.4 2.8 3.8 5.1 6.6 6.6l2.2-2.2c.3-.3.7-.4 1-.2 1.1.4 2.3.6 3.6.6.6 0 1 .4 1 1V20c0 .6-.4 1-1 1C10.6 21 3 13.4 3 4c0-.6.4-1 1-1h3.5c.6 0 1 .4 1 1 0 1.3.2 2.5.6 3.6.1.3 0 .7-.2 1l-2.3 2.2z"/></svg>
    </span>
    <span>07700 900418</span>
  </div>
</header>

<nav class="main-nav">
  <ul>
    <li class="current">Home</li>
    <li class="item">Services</li>
    <li class="item">Staff&nbsp; Menus</li>
    <li class="item">Seasonal Recipe</li>
    <li class="item">Testimonials &amp; Clients</li>
    <li class="item">About us</li>
    <li class="item">Contact us</li>
  </ul>
</nav>

<section class="hero-slider">
  <div class="hero-image" role="img" aria-label="Canapé of seared beef with salad leaf on toasted bread"></div>
  <div class="slider-arrow prev"><i><svg width="8" height="8" viewBox="0 0 8 8"><path d="M5.5 1 2.5 4l3 3" fill="none" stroke="#333" stroke-width="1.5"/></svg></i></div>
  <div class="slider-arrow next"><i><svg width="8" height="8" viewBox="0 0 8 8"><path d="M2.5 1l3 3-3 3" fill="none" stroke="#333" stroke-width="1.5"/></svg></i></div>
</section>

<aside class="testimonials">
  <h2 class="section-title">Testimonials</h2>
  <div class="testimonial first">
    <blockquote><span class="q">&ldquo;</span> Thanks so much for a superb meal on Saturday. It quite made the evening for Edwin and I to have you in the kitchen. <span class="q">&rdquo;</span></blockquote>
    <cite>Edwin and Clara Pellow</cite>
  </div>
  <div class="testimonial-divider"></div>
  <div class="testimonial">
    <blockquote><span class="q">&ldquo;</span> Thanks so much for a superb meal on Saturday. It quite made the evening for Edwin and I to have you in the kitchen. <span class="q">&rdquo;</span></blockquote>
    <cite>Edwin and Clara Pellow</cite>
  </div>
</aside>
<div class="column-divider"></div>

<section class="intro">
  <h2 class="section-title title-rule">Thimble Catering</h2>
  <p>Hello, we're Maren and Tobias, co-owners of Thimble Catering. We are a small, but perfectly formed team of Larkfield's trained chefs passionate about top quality ingredients and good food. Based in West London, we offer bespoke catering services for corporate and private events. Whether you're after cold finger food for a working lunch, a fine-dining experience for a group of close friends or creative and nutritious snacks for a children's party, we can deliver a culinary experience that delights.</p>
</section>

<section class="recipes">
  <h2 class="section-title title-rule">Seasonal Recipe Model</h2>
  <div class="recipe-strip">
    <svg class="strip-arrow prev" width="22" height="26" viewBox="0 0 22 26"><path d="M17 3 6 13l11 10" fill="none" stroke="#8cc85a" stroke-width="5"/></svg>
    <div class="recipe-thumb thumb-1" role="img" aria-label="Seared scallop on a white spoon with chive"></div>
    <div class="recipe-thumb thumb-2" role="img" aria-label="Roasted tomato canapés on a dark slate"></div>
    <div class="recipe-thumb thumb-3" role="img" aria-label="Smoked salmon blinis beside pink roses"></div>
    <svg class="strip-arrow next" width="22" height="26" viewBox="0 0 22 26"><path d="M5 3l11 10L5 23" fill="none" stroke="#8cc85a" stroke-width="5"/></svg>
  </div>
</section>

<footer class="site-footer">
  <span>Privacy Policy</span><span>|</span><span>Terms &amp; Conditions</span><span>|</span><span>Contact Us</span>
</footer>

</body>
</html>
```